Verdant Row

Currently www.verdantrow-example.com. This site was designed with a generic templet. However it is functional. I'm looking for a fun, fresh, and professional design. I also need help getting the XML for Searchly and Findo. I'm not a web designer and need help. I do not like my current sites narrow width.
Updates

All and all I'm liking the designs. The earlier ones seem better. Some seem that they are just taking my images and inputing them into a templet. I could have done that. The pictures are nice. Please keep in mind, functionality and updates. Please help us show our customers our how we are different. Safe Reliable Responsible are the key fundamentals, inside of these fundamentals show that were are customer service specialized. We are, Licensed, Insured, Drug Screened, Criminally Screened. Seems that people are putting up nice pictures but not capturing our values. Please help us market us on our website. Show our prospective customers why we are better, how we differentiate ourself from the competitors. Why choose us? Our flyers and cards are designed to drive our prospective customers to the website. If it looks identical with no pazaz like the card, then the marketing chain failed. I included our cards to help guide the thought process of our company. The link below is a feature I would love to have. This may be another project itself. I'm not sure if PX is the place to accomplish it. Below is a link for people to estimate there lawns with globe viewer. I would like to give a range of estimates using this technology. I have no clue how to accomplish it. If anyone knows how to who could do this, Please let me know. https://www.yardquoter-example.com/showOrder/MOWLAWN/propertyDetails

Target Market(s)

We target residential customers 30-80 yr old. We also are expanding and placing a special emphasis on Business accounts. The main service is a mowing and landscape maintenance. Should be the main focus of the site.

Industry/Entity Type

Searchly

Coding

Coded - Design and coding required

Font styles to use
Sans Serif

Requirements
Must have
• I want this site to be fun and colorful. It still needs to be professional looking as not to deter business accounts. If you use photos, they must reflect Florida lawn. Note the architecture the homes, grass type, types of plants.
Should not have
• My current site is ok. I use it just as a

```html
<!DOCTYPE html>
<html lang="en">
<head>
<meta charset="utf-8">
<title>Verdant Row — Lawn &amp; Grounds Maintenance</title>
<link rel="stylesheet" href="https://fonts.googleapis.com/css2?family=Open+Sans:wght@400;600;700&display=swap">
<style>
:root{
  --green:#4f8a1c;
  --green-bright:#5a9a1f;
  --red:#e2402b;
  --red-dark:#c7321f;
  --ink:#2b2b2b;
  --muted:#444;
  --panel:#e6e6e6;
  --panel-light:#f3f3f3;
  --btn-grey:#555555;
  --footer:#30301f;
  --footer-base:#e9e9e9;
  --frame:#3a3a3a;
}
*{box-sizing:border-box;margin:0;padding:0}
html,body{width:1200px;height:2292px;overflow:hidden}
body{font-family:"Open Sans",Arial,sans-serif;color:var(--ink);background:#fff;position:relative}

/* Hero */
.hero{position:absolute;left:0;top:0;width:1200px;height:658px;border-bottom:8px solid var(--green-bright)}
.hero-photo{position:absolute;inset:0;background:
  radial-gradient(ellipse 340px 300px at 200px 220px,#7a2a4a 0%,rgba(122,42,74,0) 70%),
  radial-gradient(ellipse 500px 400px at 420px 300px,#3f6a16 0%,rgba(63,106,22,0) 75%),
  radial-gradient(ellipse 600px 420px at 900px 260px,#c8e25a 0%,rgba(200,226,90,0) 70%),
  linear-gradient(160deg,#2f5210 0%,#6f9f22 45%,#a8cc3a 70%,#577f1a 100%)}
.call{position:absolute;right:112px;top:14px;display:flex;align-items:center;gap:8px;color:var(--red)}
.call-text{font-weight:700;line-height:1;text-shadow:0 1px 2px rgba(0,0,0,.35)}
.call-label{font-size:21px}
.call-number{font-size:22px;margin-top:3px}
.nav-band{position:absolute;left:0;top:71px;width:1200px;height:74px;background:rgba(255,255,255,.55);border-top:1px solid rgba(255,255,255,.8);border-bottom:1px solid rgba(255,255,255,.8)}
.brand{position:absolute;left:116px;top:20px;display:flex;align-items:center;gap:10px}
.brand-mark{width:22px;height:22px;background:var(--red)}
.brand-name{font-size:26px;font-weight:700;color:var(--green)}
.nav{position:absolute;left:577px;top:0;height:74px;display:flex;list-style:none}
.nav li{height:74px;display:flex;align-items:center;justify-content:center;border-left:1px solid rgba(120,120,120,.45);font-size:13px;font-weight:600;color:#333;text-transform:uppercase}
.nav li:last-child{border-right:1px solid rgba(120,120,120,.45)}
.nav .home{width:75px;background:var(--red);color:#fff}
.nav .about{width:78px}.nav .services{width:92px}.nav .estimate{width:95px}.nav .contact{width:115px}.nav .search{width:73px}
.slide-arrow{position:absolute;top:342px;width:52px;height:56px;background:rgba(255,255,255,.55);display:flex;align-items:center;justify-content:center}
.slide-arrow.prev{left:0}.slide-arrow.next{right:0}
.hero-title{position:absolute;right:96px;top:334px;text-align:right;font-size:68px;line-height:78px;color:#fff;font-weight:400;text-shadow:0 2px 6px rgba(0,0,0,.55)}
.estimate-btn{position:absolute;left:918px;top:614px;width:115px;height:36px;background:var(--red);color:#fff;font-size:15px;font-weight:700;display:flex;align-items:center;justify-content:center;border-radius:14px 14px 0 0}

/* Services */
.services{position:absolute;left:0;top:658px;width:1200px;height:519px;background:var(--panel)}
.section-title{text-align:center;font-size:40px;font-weight:400;color:#333}
.services .section-title{margin-top:34px}
.card{position:absolute;top:113px;width:238px;text-align:center}
.card-photo{height:154px;border:3px solid var(--frame)}
.card-photo.active{border-color:var(--red)}
.card-title{margin-top:18px;font-size:16px;font-weight:400;text-transform:uppercase;color:#222}
.card-text{margin-top:4px;font-size:12.5px;line-height:15px;color:#333;padding:0 6px}
.btn{display:inline-flex;align-items:center;justify-content:center;background:var(--btn-grey);color:#fff;font-size:13px}
.card .btn{margin-top:13px;width:96px;height:31px}
.card .btn.green{background:var(--green-bright)}
.view-all{position:absolute;left:533px;top:444px;width:138px;height:44px;font-size:15px}

/* Welcome */
.welcome{position:absolute;left:0;top:1177px;width:1200px;height:464px;background:var(--panel-light);text-align:center}
.welcome-title{margin-top:40px;font-size:52px;font-weight:400;color:#222}
.welcome-title .accent-green{color:var(--green-bright)}
.welcome-title .accent-red{color:var(--red)}
.welcome-tagline{margin-top:6px;font-size:25px;color:#222}
.welcome-copy{width:960px;margin:26px auto 0;font-size:12.5px;line-height:16px;color:#333}
.welcome-copy p{margin-bottom:11px}
.read-more{position:absolute;left:533px;top:354px;width:138px;height:44px;font-size:15px}

/* Gallery */
.gallery{position:absolute;left:0;top:1641px;width:1200px;height:550px;background:var(--panel)}
.gallery .section-title{margin-top:36px}
.gallery-rule{position:absolute;left:98px;top:105px;width:1004px;height:2px;background:#9a9a9a}
.tile{position:absolute;width:238px;height:153px;border:3px solid var(--frame)}
.tile.active{border-color:var(--red)}
.tile-zoom{position:absolute;left:50%;top:50%;transform:translate(-50%,-50%)}

/* Footer */
.footer{position:absolute;left:0;top:2191px;width:1200px;height:59px;background:var(--footer)}
.footer-links{position:absolute;left:115px;top:20px;font-size:15px;color:#fff}
.pay{position:absolute;left:944px;top:19px;display:flex;gap:4px}
.pay span{width:32px;height:21px;background:#fff;border-radius:2px}
.footer-base{position:absolute;left:0;top:2250px;width:1200px;height:42px;background:var(--footer-base)}
.copyright{position:absolute;left:105px;top:13px;font-size:14px;color:#333}
</style>
</head>
<body>

<header class="hero">
  <div class="hero-photo" role="img" aria-label="Sunny Florida garden with pink fuchsia blossoms in the foreground and a white lawn chair on green grass"></div>

  <div class="call">
    <svg width="40" height="34" viewBox="0 0 40 34" aria-hidden="true">
      <path d="M4 10 Q20 0 36 10 L33 16 L26 14 L25 10 Q20 8 15 10 L14 14 L7 16 Z" fill="#e2402b"/>
      <rect x="9" y="17" width="22" height="15" rx="3" fill="#e2402b"/>
      <circle cx="20" cy="24" r="4" fill="#fff"/>
    </svg>
    <div class="call-text">
      <div class="call-label">Call Us:</div>
      <div class="call-number">800-555-0142</div>
    </div>
  </div>

  <div class="nav-band">
    <div class="brand"><span class="brand-mark"></span><span class="brand-name">Verdant Row</span></div>
    <ul class="nav">
      <li class="home">Home</li>
      <li class="about">About</li>
      <li class="services">Services</li>
      <li class="estimate">Estimate</li>
      <li class="contact">Contact Us</li>
      <li class="search">
        <svg width="28" height="28" viewBox="0 0 28 28" aria-label="Search"><circle cx="11" cy="11" r="8" fill="none" stroke="#333" stroke-width="2.5"/><line x1="17" y1="17" x2="25" y2="25" stroke="#333" stroke-width="3" stroke-linecap="round"/></svg>
      </li>
    </ul>
  </div>

  <div class="slide-arrow prev"><svg width="16" height="24" viewBox="0 0 16 24"><polyline points="12,3 4,12 12,21" fill="none" stroke="#333" stroke-width="2.5"/></svg></div>
  <div class="slide-arrow next"><svg width="16" height="24" viewBox="0 0 16 24"><polyline points="4,3 12,12 4,21" fill="none" stroke="#333" stroke-width="2.5"/></svg></div>

  <h1 class="hero-title">Lawn &amp; Grounds<br>Maintenance</h1>
  <div class="estimate-btn">GET ESTIMATE</div>
</header>

<section class="services">
  <h2 class="section-title">Services</h2>

  <article class="card" style="left:98px">
    <div class="card-photo active" role="img" aria-label="Red riding mower on a freshly cut lawn" style="background:linear-gradient(170deg,#6c8c3a 0%,#4e7a22 55%,#3c6318 100%)"></div>
    <h3 class="card-title">Lawn Care</h3>
    <p class="card-text">Lorem Ipsum is simply dummy text of the printing and typesetting industry.Lorem Ipsum is simply...</p>
    <span class="btn green">Read More</span>
  </article>

  <article class="card" style="left:354px">
    <div class="card-photo" role="img" aria-label="Gloved hands planting flowers in a garden bed" style="background:linear-gradient(160deg,#5f7d2c 0%,#4a3a26 60%,#2f2418 100%)"></div>
    <h3 class="card-title">Flower Bed Maintenance</h3>
    <p class="card-text">Lorem Ipsum is simply dummy text of the printing and typesetting industry.Lorem Ipsum is simply...</p>
    <span class="btn">Read More</span>
  </article>

  <article class="card" style="left:608px">
    <div class="card-photo" role="img" aria-label="Neatly trimmed hedge beside a house" style="background:linear-gradient(180deg,#dfe7ee 0%,#c9d3da 30%,#3b5a22 45%,#2c4a18 80%,#6a9a30 100%)"></div>
    <h3 class="card-title">Trimming and Pruning</h3>
    <p class="card-text">Lorem Ipsum is simply dummy text of the printing and typesetting industry.Lorem Ipsum is simply...</p>
    <span class="btn">Read More</span>
  </article>

  <article class="card" style="left:862px">
    <div class="card-photo" role="img" aria-label="Pressure washer cleaning a wooden deck" style="background:linear-gradient(165deg,#b77a4c 0%,#a0623a 45%,#c99a72 70%,#8a5530 100%)"></div>
    <h3 class="card-title">Power Washing</h3>
    <p class="card-text">Lorem Ipsum is simply dummy text of the printing and typesetting industry.Lorem Ipsum is simply...</p>
    <span class="btn">Read More</span>
  </article>

  <span class="btn view-all">View All</span>
</section>

<section class="welcome">
  <h2 class="welcome-title">Welcome to <span class="accent-green">Verdant</span> <span class="accent-red">Row</span></h2>
  <p class="welcome-tagline">" Your Year Around Lawn Care Solution "</p>
  <div class="welcome-copy">
    <p>Verdant Row is SAFE, Reliable, and Responsible. We make sure that all of our lawn care professionals are licensed, insured, drug-free, background checks completed and legally eligible to work.</p>
    <p>Verdant Row offers convenient online bill pay, we accepts credit cards, and we pride ourselves with a great customer service department.</p>
    <p>If you are tired of lawn service companies that deliver poor quality, never call you back, have lousy communication skills, and are generally unprofessional and unreliable please consider giving Verdant Row a try.</p>
    <p>Try us with no risk and zero commitment. If you are not completely wowed by our unique service you may walk away without any pressure or hassle.</p>
  </div>
  <span class="btn read-more">Read more</span>
</section>

<section class="gallery">
  <h2 class="section-title">Project Gallery</h2>
  <div class="gallery-rule"></div>

  <div class="tile active" role="img" aria-label="Freshly washed wooden deck" style="left:98px;top:128px;background:linear-gradient(170deg,#7a8a5a 0%,#a0643c 40%,#b5784a 100%)">
    <svg class="tile-zoom" width="70" height="70" viewBox="0 0 70 70" aria-hidden="true"><circle cx="30" cy="30" r="20" fill="none" stroke="rgba(255,255,255,.75)" stroke-width="4"/><line x1="45" y1="45" x2="62" y2="62" stroke="rgba(255,255,255,.75)" stroke-width="6" stroke-linecap="round"/></svg>
  </div>
  <div class="tile" role="img" aria-label="Striped lawn with colourful flower beds" style="left:354px;top:128px;background:linear-gradient(180deg,#6a8a3a 0%,#c25a6a 30%,#3f8a22 45%,#5aa42a 100%)"></div>
  <div class="tile" role="img" aria-label="Garden hose watering the grass" style="left:608px;top:128px;background:linear-gradient(160deg,#9acb4a 0%,#6ea02c 60%,#4f7e1c 100%)"></div>
  <div class="tile" role="img" aria-label="Curving lawn edged with red flower beds" style="left:862px;top:128px;background:linear-gradient(170deg,#3b5e1c 0%,#c23a2a 35%,#4c8a22 55%,#6aa52e 100%)"></div>

  <div class="tile" role="img" aria-label="Push mower cutting a green lawn" style="left:98px;top:300px;background:linear-gradient(170deg,#4a6a2a 0%,#5f9a24 50%,#7ab832 100%)"></div>
  <div class="tile" role="img" aria-label="Sprinkler spraying water over a lawn" style="left:354px;top:300px;background:linear-gradient(160deg,#2f4a22 0%,#7a8a7a 45%,#4a7a26 100%)"></div>
  <div class="tile" role="img" aria-label="Large Florida home with manicured front lawn" style="left:608px;top:300px;background:linear-gradient(180deg,#c9dbe8 0%,#b9a88a 40%,#8a7a62 55%,#5a9a2a 75%,#4a8a22 100%)"></div>
  <div class="tile" role="img" aria-label="Garden path winding through a green lawn" style="left:862px;top:300px;background:linear-gradient(180deg,#dfe9ee 0%,#5a8a3a 35%,#6aa830 65%,#c9c2b0 100%)"></div>
</section>

<footer>
  <div class="footer">
    <div class="footer-links">| Home | About | Services | Estimate | Contact Us |</div>
    <div class="pay" aria-label="Accepted payment cards"><span></span><span></span><span></span><span></span></div>
  </div>
  <div class="footer-base">
    <p class="copyright">Copyright Verdant Row 2014. All Rights Reserved.</p>
  </div>
</footer>

</body>
</html>
```